QLB Insurance Services Business Card
Slogan - Quiet Lanterns Burn
Creative Brief
Use specific fonts
Feel free to use the same font as used in my logo OR whatever looks good
Simple
Marisol (Greta) Dovik
Broker
20387 Marlowpine Dr. Tustin, CA 92740
greta@qlbinsurance.example
www.qblinsurance.example
0K47382
*Commercial Liability *Commercial Property *Business Owner Policy *Excess/Umbrella Liability *Worker's Compensation *Professional Liability *Commercial/Business Auto *Homeowner/Auto Insurance *Flood/Earthquake Insurance and more *Specializing import/export and manufacture company

```html
<!DOCTYPE html>
<html lang="en">
<head>
<meta charset="utf-8">
<title>QLB Insurance Services – Business Card</title>
<link href="https://fonts.googleapis.com/css2?family=Cinzel:wght@500;700&family=Open+Sans:ital,wght@0,400;0,600;1,600&family=Crimson+Text:wght@400;600&display=swap" rel="stylesheet">
<style>
  :root{
    --page:#e9e6e1;
    --card:#ffffff;
    --ink:#1d1d1f;
    --muted:#4a4a4a;
    --blue:#2a8fd6;
    --blue-deep:#1468b0;
    --blue-light:#7cc4f2;
    --rule:#9a9a9a;
  }
  *{box-sizing:border-box;margin:0;padding:0}
  html,body{width:1200px;height:780px;overflow:hidden;background:var(--page)}
  .canvas{width:1200px;height:780px;display:flex;align-items:center;justify-content:center}
  .card{
    position:relative;width:1050px;height:600px;background:var(--card);
    border-radius:28px;overflow:hidden;box-shadow:0 10px 30px rgba(0,0,0,.18);
    font-family:"Crimson Text",Georgia,serif;color:var(--ink);
  }
  .edge-band{position:absolute;top:0;bottom:0;width:34px;
    background:linear-gradient(90deg,var(--blue-deep),var(--blue),var(--blue-light))}
  .edge-band--left{left:0}
  .edge-band--right{right:0;transform:scaleX(-1)}
  .edge-line{position:absolute;top:0;bottom:0;width:4px;background:var(--ink)}
  .edge-line--left{left:44px}
  .edge-line--right{right:44px}

  .brand{position:absolute;top:44px;left:0;right:0;text-align:center}
  .brand-mark{display:inline-flex;align-items:center;gap:14px;
    font-family:"Cinzel",serif;font-weight:700;font-size:64px;color:var(--ink);letter-spacing:4px}
  .brand-dot{width:22px;height:22px;border-radius:50%;background:var(--blue)}
  .company{margin-top:10px;font-family:"Cinzel",serif;font-weight:500;font-size:50px;letter-spacing:1px;line-height:1}
  .company-rule{width:560px;height:3px;margin:10px auto 6px;background:var(--blue)}
  .slogan{font-family:"Open Sans",sans-serif;font-weight:600;font-size:30px;color:var(--blue);letter-spacing:.5px}

  .person{position:absolute;top:320px;left:0;right:0;text-align:center;padding-left:120px}
  .person-name{font-family:"Open Sans",sans-serif;font-style:italic;font-weight:600;font-size:36px;color:var(--blue)}
  .person-sep{font-family:"Open Sans",sans-serif;font-size:36px;color:var(--ink);margin:0 10px}
  .person-role{font-family:"Open Sans",sans-serif;font-size:24px;color:var(--ink);vertical-align:4px}
  .license{margin-top:6px;font-size:25px;color:var(--muted)}

  .contact{position:absolute;left:90px;right:90px;top:438px;height:110px;
    border-top:1.5px solid var(--rule);display:flex;align-items:center}
  .contact-block{height:88px;display:flex;flex-direction:column;justify-content:center;gap:8px;font-size:26px;color:var(--muted)}
  .address{width:230px;line-height:1.2}
  .divider{width:1.5px;height:88px;background:var(--rule);margin:0 18px}
  .phones{width:190px}
  .online{flex:1}
  .row{display:flex;align-items:center;gap:10px;line-height:1}
  .icon{width:24px;height:24px;flex:none}
</style>
</head>
<body>
<main class="canvas">
  <section class="card">
    <div class="edge-band edge-band--left"></div>
    <div class="edge-line edge-line--left"></div>
    <div class="edge-band edge-band--right"></div>
    <div class="edge-line edge-line--right"></div>

    <header class="brand">
      <div class="brand-mark"><span class="brand-dot"></span>QLB</div>
      <h1 class="company">QLB Insurance Services</h1>
      <div class="company-rule"></div>
      <p class="slogan">QuietLanternsBurn</p>
    </header>

    <div class="person">
      <span class="person-name">Marisol (Greta) Dovik</span><span class="person-sep">/</span><span class="person-role">Broker</span>
      <p class="license">License No : 0K47382</p>
    </div>

    <footer class="contact">
      <div class="contact-block address">
        <span>20387 Marlowpine</span>
        <span>Dr. Tustin, CA 92740</span>
      </div>
      <div class="divider"></div>
      <div class="contact-block phones">
        <div class="row">
          <svg class="icon" viewBox="0 0 24 24"><path fill="var(--blue)" d="M6.6 10.8a15 15 0 0 0 6.6 6.6l2.2-2.2c.3-.3.7-.4 1-.2 1.1.4 2.3.6 3.6.6.6 0 1 .4 1 1V20c0 .6-.4 1-1 1A17 17 0 0 1 3 4c0-.6.4-1 1-1h3.5c.6 0 1 .4 1 1 0 1.3.2 2.5.6 3.6.1.3 0 .7-.2 1z"/></svg>
          <span>949-555-0148</span>
        </div>
        <div class="row">
          <svg class="icon" viewBox="0 0 24 24"><rect x="3" y="9" width="18" height="11" rx="2" fill="var(--blue)"/><rect x="6" y="3" width="12" height="7" fill="none" stroke="var(--blue)" stroke-width="2"/><rect x="7" y="12" width="10" height="2" fill="#fff"/></svg>
          <span>949-555-0193</span>
        </div>
      </div>
      <div class="divider"></div>
      <div class="contact-block online">
        <div class="row">
          <svg class="icon" viewBox="0 0 24 24"><circle cx="12" cy="12" r="11" fill="var(--blue)"/><circle cx="12" cy="12" r="4" fill="none" stroke="#fff" stroke-width="2"/><path d="M16 12v1.5a2 2 0 0 0 4 0V12a8 8 0 1 0-3 6.2" fill="none" stroke="#fff" stroke-width="2"/></svg>
          <span>greta@qlbinsurance.example</span>
        </div>
        <div class="row">
          <svg class="icon" viewBox="0 0 24 24"><circle cx="12" cy="12" r="11" fill="var(--blue)"/><g fill="none" stroke="#fff" stroke-width="1.5"><circle cx="12" cy="12" r="7"/><ellipse cx="12" cy="12" rx="3" ry="7"/><path d="M5 12h14"/></g></svg>
          <span>www.qlbinsurance.example</span>
        </div>
      </div>
    </footer>
  </section>
</main>
</body>
</html>
```